Updated website design needed for Radiology Group, Pinecrest Valley Imaging Partners

Clean, uncluttered, updated design needed for top regional Radiology Center. Focus on personal, patient oriented design, (not clinical). Should be simple and easy to navigate, with clear CTAs. Use blues, greens and photos of people in the Central Oregon outdoors.
Uncoded, PSD design only. 2 pages: Home page and one example interior page.
reference current site: http://www.pvipxq.com/
Sites they like:
http://www.hollowbrookscan.com/
http://www.mdlq.net/handler.cfm?event=practice,main
http://www.elmtidejoint.com/

Industry/Entity Type

Medical Imaging

Number of Pages Required

2 page

Font styles to use
Sans Serif

Requirements
Must have
• Personal and patient friendly.
• Lots of white space, clean and uncluttered. Clear CTAs, such as: Patient Bill Pay, Make an Appointment, Meet Our Doctors
• Use copy and contact information from the current site.
• Use outdoor images from Central Oregon, late Winter/ Spring (snow, light colors, spring green, for example)
• Include one example interior page, either Your Exam or Meet Our Doctors
Nice to have
• The client likes:
• Meet Our Doctors slider section, and big, easy to navigate Information Center on www.elmtidejoint.com
• The personal feel of the Your Exam section on www.hollowbrookscan.com
• Blues and Greens, outdoorsy imagery
Should not have
• The client does not like:
• complex drop down menus
• clinical feel
• Do not use lorum ipsum or dummy text.
• Do not use outdoor images from other regions. Do not use Summer (hot, poolside) or Fall (red/orange leaves) images.

```html
<!DOCTYPE html>
<html lang="en">
<head>
<meta charset="utf-8">
<title>Pinecrest Valley Imaging Partners</title>
<link href="https://fonts.googleapis.com/css2?family=Lato:wght@300;400;700;900&family=Open+Sans:wght@400;600;700&display=swap" rel="stylesheet">
<style>
:root{
  --teal:#10a3c6;
  --teal-dark:#0b8fae;
  --green:#8dbb10;
  --green-dark:#6f9a08;
  --ink:#222;
  --text:#444;
  --muted:#777;
  --grey-band:#eeeeee;
  --footer:#2e2e2e;
  --line:#d9d9d9;
  --white:#fff;
}
*{box-sizing:border-box;margin:0;padding:0}
html,body{width:1200px;height:3448px;overflow:hidden}
body{position:relative;background:var(--white);font-family:"Open Sans",Arial,sans-serif;color:var(--text)}
.abs{position:absolute}
h1,h2,h3,h4{font-family:"Lato",Arial,sans-serif;font-weight:400}

/* header */
.brand{left:80px;top:12px;height:74px;display:flex;align-items:center;gap:12px}
.brand-mark{width:62px;height:62px;background:#3e4f8a}
.brand-name{font-family:"Lato",sans-serif;font-weight:700;color:#2b3566;font-size:18px;line-height:21px;width:170px}
.contact-chip{top:18px;height:56px;border:2px solid var(--line);border-radius:6px;display:flex;align-items:center;gap:10px;padding:0 10px;background:#fff}
.contact-chip .ico{width:38px;height:38px;border-radius:50%;background:var(--teal);display:flex;align-items:center;justify-content:center}
.contact-chip b{display:block;color:var(--teal);font-size:14px;font-weight:700}
.contact-chip span{font-size:14px;color:#333}
.online-dot{left:912px;top:36px;width:18px;height:18px;border-radius:50%;background:var(--green)}
.btn-top{top:28px;height:36px;border-radius:3px;color:#fff;font-size:14px;display:flex;align-items:center;justify-content:center}
.btn-register{left:952px;width:80px;background:var(--green)}
.btn-login{left:1039px;width:81px;background:var(--teal)}

.main-nav{left:0;top:92px;width:1200px;height:40px;background:var(--teal)}
.main-nav ul{list-style:none;display:flex;position:absolute;left:80px;top:0;height:40px}
.main-nav li{font-size:14px;color:#fff;height:40px;line-height:40px;padding:0 12px;border-right:1px solid rgba(255,255,255,.35);position:relative}
.main-nav li:last-child{border-right:0}
.main-nav li.active{background:var(--teal-dark);font-weight:700}
.main-nav li.active::after{content:"";position:absolute;left:50%;bottom:-8px;margin-left:-8px;border:8px solid transparent;border-bottom:0;border-top-color:var(--teal-dark)}

/* hero */
.hero{left:0;top:132px;width:1200px;height:628px;background:linear-gradient(180deg,#8fb9d8 0%,#c9dbe6 28%,#e7eef1 40%,#6f8a78 52%,#3f6a4f 72%,#2e5a3c 100%)}
.hero-title{left:0;top:370px;width:1200px;text-align:center;font-family:"Lato",sans-serif;font-weight:700;font-size:39px;line-height:48px;color:#fff;text-shadow:0 2px 6px rgba(0,0,0,.55)}
.hero-cta{left:482px;top:497px;width:236px;height:46px;background:var(--green);color:#fff;font-size:18px;display:flex;align-items:center;justify-content:center;border-radius:2px}
.slider-arrow{top:736px;width:46px;height:46px;border-radius:50%;background:var(--green);display:flex;align-items:center;justify-content:center}

/* services */
.services{left:80px;top:593px;width:1040px;height:310px;display:flex}
.service{width:260px;height:310px;color:#fff;position:relative;padding:22px 0 0 0;text-align:center}
.service.teal{background:var(--teal)}
.service.green{background:var(--green)}
.service .icon-box{width:74px;height:74px;margin:0 auto 10px;border:3px solid #fff;border-radius:8px;display:flex;align-items:center;justify-content:center}
.service h3{font-family:"Lato",sans-serif;font-weight:700;font-size:20px;line-height:26px;margin-bottom:14px}
.service ul{list-style:none;text-align:left;padding-left:56px;font-size:12.5px;line-height:24px}
.service li::before{content:"• "}
.service .more{position:absolute;left:112px;bottom:-16px;width:34px;height:34px;border-radius:50%;background:#fff;color:var(--teal);font-weight:700;font-size:22px;line-height:32px;text-align:center}
.service.green .more{color:var(--green)}

/* section titles */
.section-title{font-family:"Lato",sans-serif;font-size:38px;color:var(--ink)}
.section-title strong{color:var(--teal);font-weight:700}
.bar-title{padding-left:16px;border-left:6px solid var(--teal)}

/* info center */
.info-title{left:0;top:950px;width:1200px;text-align:center}
.info-grid{left:80px;top:1030px;width:1040px;display:flex}
.info-item{width:208px;text-align:center;border-right:1px solid var(--line);height:220px}
.info-item:last-child{border-right:0}
.info-item svg{display:block;margin:0 auto}
.info-item p{font-family:"Lato",sans-serif;font-weight:700;font-size:19px;line-height:25px;color:#222;margin-top:14px}

/* welcome */
.welcome-band{left:0;top:1299px;width:1200px;height:396px;background:var(--grey-band)}
.welcome-title{left:80px;top:1340px;line-height:42px}
.welcome-title span{display:block;font-size:36px;color:var(--ink)}
.welcome-title strong{display:block;font-size:32px;color:var(--teal);font-weight:700}
.welcome-copy{left:80px;top:1432px;width:640px;font-size:12.5px;line-height:26px;color:#333}
.read-more{left:80px;top:1600px;width:106px;height:40px;background:var(--green);color:#fff;font-size:15px;display:flex;align-items:center;justify-content:center}
.video{left:766px;top:1352px;width:354px;height:254px;background:linear-gradient(135deg,#29505c 0%,#1f3a46 50%,#3a3f44 100%)}
.video-title{left:790px;top:1368px;font-family:"Lato",sans-serif;font-weight:900;font-size:16px;color:#fff}
.play{left:916px;top:1456px;width:54px;height:54px;border-radius:50%;background:rgba(0,0,0,.55);display:flex;align-items:center;justify-content:center}

/* doctors */
.doctors-title{left:80px;top:1742px}
.doctor-cards{left:80px;top:1821px;width:1040px;display:flex;gap:46px}
.doctor{width:226px;height:278px;background:#f2f2f2;border-bottom:4px solid var(--teal);text-align:center}
.doctor .photo{height:188px}
.doctor h4{font-family:"Lato",sans-serif;font-weight:700;font-size:18px;color:var(--green);margin-top:14px}
.doctor p{font-size:15px;color:#333;margin-top:4px}
.chev{top:1930px}

/* testimonials */
.testi-ring{left:80px;top:2161px;width:300px;height:320px}
.testi-title{left:398px;top:2190px}
.testi-quote{left:398px;top:2270px;width:722px;font-style:italic;font-size:13px;line-height:26px;color:#555}
.testi-name{left:398px;top:2412px;font-size:14px;font-weight:700;color:var(--green)}
.testi-dots{left:398px;top:2449px;display:flex;gap:10px;align-items:center}
.testi-dots i{width:9px;height:9px;border-radius:50%;background:var(--teal);display:block}
.testi-dots i.on{width:14px;height:14px;background:var(--green)}

/* contact */
.footer-band{left:0;top:2821px;width:1200px;height:586px;background:var(--footer)}
.touch-panel{left:80px;top:2586px;width:1034px;height:414px;background:var(--teal)}
.touch-fold{left:80px;top:2586px;width:100px;height:100px}
.touch-title{left:80px;top:2604px;width:790px;text-align:center;font-family:"Lato",sans-serif;font-size:36px;color:#fff}
.touch-title strong{font-weight:700}
.field{height:36px;background:#fff;border:1px solid #cfcfcf;font-size:12px;color:#999;padding:10px 14px}
.submit{left:195px;top:2922px;width:580px;height:38px;background:var(--green);color:#fff;font-style:italic;font-size:15px;display:flex;align-items:center;justify-content:center}
.doctor-standing{left:880px;top:2471px;width:270px;height:529px;background:linear-gradient(180deg,#f3f6f8 0%,#e6edf2 40%,#d4dde6 100%)}

/* footer */
.f-head{font-family:"Lato",sans-serif;font-size:19px;color:#fff}
.f-head strong{color:var(--green);font-weight:400}
.f-list{list-style:none;font-size:13px;line-height:28px;color:#fff}
.f-list li::before{content:"• ";color:var(--green)}
.f-text{font-size:13px;line-height:28px;color:#fff}
.f-label{color:var(--green)}
.hours{left:853px;top:3035px;width:267px;height:350px;background:var(--green-dark);border:4px solid var(--green)}
.hours table{position:absolute;left:40px;top:72px;border-collapse:collapse;font-size:13px;color:#fff}
.hours td{height:30px;padding-right:18px}
.hours td:first-child{font-weight:700}
.hours-btn{left:60px;top:305px;width:145px;height:32px;background:var(--green);color:#fff;font-size:12px;display:flex;align-items:center;justify-content:center}
.copyright{left:0;top:3407px;width:1200px;height:41px;background:var(--teal);color:#fff;font-size:13px;text-align:center;line-height:41px}
</style>
</head>
<body>

<!-- Header -->
<header>
  <div class="abs brand">
    <div class="brand-mark"></div>
    <div class="brand-name">Pinecrest Valley Imaging Partners</div>
  </div>
  <div class="abs contact-chip" style="left:536px;width:184px">
    <div class="ico"><svg width="20" height="16" viewBox="0 0 20 16"><rect x="1" y="1" width="18" height="14" fill="none" stroke="#fff" stroke-width="2"/><path d="M1 1l9 8 9-8" fill="none" stroke="#fff" stroke-width="2"/></svg></div>
    <div><b>Mail Us:</b><span>info@pvipxq.com</span></div>
  </div>
  <div class="abs contact-chip" style="left:731px;width:178px">
    <div class="ico"><svg width="18" height="18" viewBox="0 0 24 24"><path d="M6.6 10.8a15 15 0 006.6 6.6l2.2-2.2a1 1 0 011-.25 11.4 11.4 0 003.6.6 1 1 0 011 1V20a1 1 0 01-1 1A17 17 0 013 4a1 1 0 011-1h3.5a1 1 0 011 1 11.4 11.4 0 00.6 3.6 1 1 0 01-.25 1z" fill="#fff"/></svg></div>
    <div><b>Main Line:</b><span>(555) 382-6633</span></div>
  </div>
  <div class="abs online-dot"></div>
  <div class="abs btn-top btn-register">Register</div>
  <div class="abs btn-top btn-login">Log In</div>
</header>

<nav class="abs main-nav">
  <ul>
    <li class="active">Home</li><li>About Us</li><li>Our Services</li><li>For Patients</li><li>Our Physicians</li><li>For Physicians</li><li>PACS &amp; Documents</li><li>Appointments</li><li>Our Locations</li>
  </ul>
</nav>

<!-- Hero -->
<section>
  <div class="abs hero" role="img" aria-label="Snow-capped Central Oregon mountains above a pine forest and calm lake in late winter"></div>
  <h1 class="abs hero-title">All Technologists Have Advanced Level Training &amp;<br>Certifications In Modalities They Specialize In.</h1>
  <div class="abs hero-cta">Make An Appointment</div>
  <div class="abs slider-arrow" style="left:48px"><svg width="14" height="14" viewBox="0 0 14 14"><path d="M9 2L4 7l5 5" fill="none" stroke="#fff" stroke-width="2.5"/></svg></div>
  <div class="abs slider-arrow" style="left:1106px"><svg width="14" height="14" viewBox="0 0 14 14"><path d="M5 2l5 5-5 5" fill="none" stroke="#fff" stroke-width="2.5"/></svg></div>

  <div class="abs services">
    <div class="service teal">
      <div class="icon-box"><svg width="40" height="40" viewBox="0 0 40 40"><rect x="6" y="4" width="28" height="32" fill="none" stroke="#fff" stroke-width="2.5"/><path d="M20 10v20M13 15h14M13 20h14M13 25h14" stroke="#fff" stroke-width="2"/></svg></div>
      <h3>General<br>Radiology</h3>
      <ul><li>Head, chest, abdomen</li><li>Upper &amp; lower extremity</li><li>Fluoroscopy:</li><li>Barium Enema</li><li>Myelography</li></ul>
      <div class="more">+</div>
    </div>
    <div class="service green">
      <div class="icon-box"><svg width="40" height="40" viewBox="0 0 40 40"><rect x="8" y="24" width="24" height="10" fill="none" stroke="#fff" stroke-width="2.5"/><path d="M14 24V8h12v16" fill="none" stroke="#fff" stroke-width="2.5"/></svg></div>
      <h3>Digital<br>Mammography</h3>
      <ul><li>Screening</li><li>Diagnostic</li><li>Stereotactic biopsy</li><li>Ductography</li><li>Needle localizations</li></ul>
      <div class="more">+</div>
    </div>
    <div class="service teal">
      <div class="icon-box"><svg width="40" height="40" viewBox="0 0 40 40"><circle cx="20" cy="18" r="12" fill="none" stroke="#fff" stroke-width="2.5"/><circle cx="20" cy="18" r="5" fill="none" stroke="#fff" stroke-width="2.5"/><path d="M6 34h28" stroke="#fff" stroke-width="2.5"/></svg></div>
      <h3>Computed<br>Tamography</h3>
      <ul><li>Abdomen/Pelvis</li><li>Chest</li><li>Head &amp; sinus</li><li>Upper &amp; lower extremity</li><li>Angiography</li></ul>
      <div class="more">+</div>
    </div>
    <div class="service green">
      <div class="icon-box"><svg width="40" height="40" viewBox="0 0 40 40"><path d="M6 32V18a14 14 0 0128 0v14z" fill="none" stroke="#fff" stroke-width="2.5"/><circle cx="20" cy="20" r="6" fill="none" stroke="#fff" stroke-width="2.5"/></svg></div>
      <h3>Magnetic<br>Resonance Imaging</h3>
      <ul><li>Musculoskeletal</li><li>Brain</li><li>Spine</li><li>Abdomen</li><li>Breast</li></ul>
      <div class="more">+</div>
    </div>
  </div>
</section>

<!-- Information Center -->
<section>
  <h2 class="abs section-title info-title">Information <strong>Center</strong></h2>
  <div class="abs info-grid">
    <div class="info-item">
      <svg width="140" height="148" viewBox="0 0 140 148"><path d="M70 4a70 70 0 000 140" fill="none" stroke="#222" stroke-width="6"/><circle cx="70" cy="74" r="50" fill="var(--green)"/><rect x="46" y="60" width="30" height="26" fill="none" stroke="#222" stroke-width="3"/><circle cx="86" cy="64" r="7" fill="#222"/><path d="M74 90a12 12 0 0124 0z" fill="#222"/></svg>
      <p>Patient<br>Portal</p>
    </div>
    <div class="info-item">
      <svg width="140" height="148" viewBox="0 0 140 148"><path d="M70 4a70 70 0 000 140" fill="none" stroke="#222" stroke-width="6"/><circle cx="70" cy="74" r="50" fill="var(--green)"/><rect x="48" y="54" width="40" height="38" fill="none" stroke="#222" stroke-width="3"/><path d="M48 64h40M58 72h6M70 72h6M58 80h6M70 80h6" stroke="#222" stroke-width="3"/><circle cx="90" cy="90" r="10" fill="var(--green)" stroke="#222" stroke-width="3"/></svg>
      <p>Request An<br>Appointment</p>
    </div>
    <div class="info-item">
      <svg width="140" height="148" viewBox="0 0 140 148"><path d="M70 4a70 70 0 000 140" fill="none" stroke="#222" stroke-width="6"/><circle cx="70" cy="74" r="50" fill="var(--green)"/><rect x="44" y="56" width="52" height="34" fill="none" stroke="#222" stroke-width="3"/><path d="M60 96h20" stroke="#222" stroke-width="3"/><rect x="54" y="66" width="22" height="14" fill="#222"/></svg>
      <p>Pay My Bill<br>Online</p>
    </div>
    <div class="info-item">
      <svg width="140" height="148" viewBox="0 0 140 148"><path d="M70 4a70 70 0 000 140" fill="none" stroke="#222" stroke-width="6"/><circle cx="70" cy="74" r="50" fill="var(--green)"/><path d="M52 96V80a20 20 0 1136 -8l-4 8v16z" fill="#222"/><text x="66" y="80" font-family="Lato,sans-serif" font-weight="900" font-size="20" fill="var(--green)">?</text></svg>
      <p>What's<br>Happening</p>
    </div>
    <div class="info-item">
      <svg width="140" height="148" viewBox="0 0 140 148"><path d="M70 4a70 70 0 000 140" fill="none" stroke="#222" stroke-width="6"/><circle cx="70" cy="74" r="50" fill="var(--green)"/><path d="M46 58h34v22H60l-8 8v-8h-6z" fill="#222"/><path d="M84 66h10v20h-4v6l-6-6H66v-4h18z" fill="#222"/></svg>
      <p>Client<br>Testimonials</p>
    </div>
  </div>
</section>

<!-- Welcome -->
<section>
  <div class="abs welcome-band"></div>
  <h2 class="abs welcome-title bar-title"><span>Welcome to</span><strong>Pinecrest Valley Imaging Partners</strong></h2>
  <p class="abs welcome-copy">Pinecrest Valley Imaging Partners is a diagnostic imaging corporation providing professional services to Central &amp; Eastern Oregon hospitals &amp; clinics as well as state-of-the-art services in its own outpatient imaging center. PVIP was established by its founder, Harold M. Whitcombe, MD when he opened his Central Oregon practice in 1947. PVIP is staffed by fellowship trained physicians with expertise in major disciplines to include mammography, ultrasound, Magnetic Resonance Imaging, Computed Tomography, Positron Emission Tomography, interventional procedures, Nuclear Medicine ...</p>
  <div class="abs read-more">Read More</div>
  <div class="abs video" role="img" aria-label="Video still introducing 3D mammography with a patient silhouette and a breast scan image"></div>
  <div class="abs video-title">WHAT IS 3D MAMOGRAPHY?</div>
  <div class="abs play"><svg width="20" height="22" viewBox="0 0 20 22"><path d="M3 2l15 9-15 9z" fill="#fff"/></svg></div>
</section>

<!-- Meet Our Doctors -->
<section>
  <h2 class="abs section-title bar-title doctors-title">Meet Our <strong>Doctors</strong></h2>
  <svg class="abs chev" style="left:28px" width="20" height="40" viewBox="0 0 20 40"><path d="M16 4L4 20l12 16" fill="none" stroke="#333" stroke-width="2"/></svg>
  <svg class="abs chev" style="left:1152px" width="20" height="40" viewBox="0 0 20 40"><path d="M4 4l12 16L4 36" fill="none" stroke="#333" stroke-width="2"/></svg>
  <div class="abs doctor-cards">
    <div class="doctor"><div class="photo" role="img" aria-label="Portrait of a female surgeon in a white coat" style="background:linear-gradient(180deg,#e9ecef,#cfd6dc)"></div><h4>Dr. Lena Marsh</h4><p>Surgeon</p></div>
    <div class="doctor"><div class="photo" role="img" aria-label="Portrait of a gynecologist in a lab cap at a microscope" style="background:linear-gradient(180deg,#eef1f4,#d6dde3)"></div><h4>Dr. Lena Marsh</h4><p>Gynecologist</p></div>
    <div class="doctor"><div class="photo" role="img" aria-label="Portrait of a surgeon wearing a blue mask" style="background:linear-gradient(180deg,#e8eef2,#c9d8e0)"></div><h4>Dr. Lena Marsh</h4><p>Surgeon</p></div>
    <div class="doctor"><div class="photo" role="img" aria-label="Portrait of a smiling male gynecologist" style="background:linear-gradient(180deg,#eceff1,#d3d9de)"></div><h4>Dr. Lena Marsh</h4><p>Gynecologist</p></div>
  </div>
</section>

<!-- Testimonials -->
<section>
  <svg class="abs testi-ring" viewBox="0 0 300 320">
    <path d="M240 10A150 150 0 00240 310" fill="none" stroke="#d8d8d8" stroke-width="10" transform="translate(-60 0)"/>
    <circle cx="150" cy="166" r="112" fill="none" stroke="var(--green)" stroke-width="4"/>
    <circle cx="228" cy="230" r="28" fill="var(--green)"/>
    <path d="M214 222h10v10l-6 10h-4l4-10h-4zM230 222h10v10l-6 10h-4l4-10h-4z" fill="#fff"/>
  </svg>
  <div class="abs" role="img" aria-label="Portrait of a smiling patient" style="left:126px;top:2223px;width:208px;height:208px;border-radius:50%;background:radial-gradient(circle at 50% 40%,#c9d3db,#5e6a73)"></div>
  <div class="abs" style="left:282px;top:2365px;width:56px;height:56px;border-radius:50%;background:var(--green);display:flex;align-items:center;justify-content:center"><svg width="26" height="20" viewBox="0 0 26 20"><path d="M1 1h10v10l-6 8H1l4-8H1zM15 1h10v10l-6 8h-4l4-8h-4z" fill="#fff"/></svg></div>
  <h2 class="abs section-title bar-title testi-title">Customer <strong>Testimonials</strong></h2>
  <p class="abs testi-quote"><span style="font-size:40px;color:#ccc;line-height:0;vertical-align:-12px">&ldquo;</span> The whole team made my mammogram feel calm and personal. The technologist explained every step, answered all my questions, and my results were shared with my doctor the very next day. Scheduling was simple, parking was easy, and I never once felt rushed during my visit. <span style="font-size:40px;color:#ccc;line-height:0;vertical-align:-18px">&rdquo;</span></p>
  <div class="abs testi-name">Mr. Owen Carraway</div>
  <div class="abs testi-dots"><i class="on"></i><i></i><i></i><i></i></div>
</section>

<!-- Get In Touch + Footer -->
<section>
  <div class="abs footer-band"></div>
  <div class="abs touch-panel"></div>
  <svg class="abs touch-fold" viewBox="0 0 100 100"><path d="M0 0h100L0 100z" fill="#fff"/><path d="M100 0L0 100h40a60 60 0 0160-60z" fill="#d9d9d9"/></svg>
  <h2 class="abs touch-title">Get In <strong>Touch</strong></h2>
  <div class="abs field" style="left:195px;top:2685px;width:283px">First Name</div>
  <div class="abs field" style="left:490px;top:2685px;width:285px">Last Name</div>
  <div class="abs field" style="left:195px;top:2736px;width:283px">Phone</div>
  <div class="abs field" style="left:490px;top:2736px;width:285px">Email</div>
  <div class="abs field" style="left:195px;top:2789px;width:580px;height:120px">Message</div>
  <div class="abs submit">Submit</div>
  <div class="abs doctor-standing" role="img" aria-label="Friendly doctor in a white coat with stethoscope, arms crossed"></div>

  <!-- Quick links -->
  <svg class="abs" style="left:80px;top:3040px" width="40" height="40" viewBox="0 0 40 40"><rect x="4" y="16" width="20" height="12" rx="6" fill="none" stroke="var(--green)" stroke-width="3" transform="rotate(-45 14 22)"/><rect x="16" y="12" width="20" height="12" rx="6" fill="none" stroke="var(--green)" stroke-width="3" transform="rotate(-45 26 18)"/></svg>
  <div class="abs f-head" style="left:80px;top:3090px">Quick <strong>Links</strong></div>
  <ul class="abs f-list" style="left:80px;top:3122px">
    <li>Home</li><li>About Us</li><li>Our Services</li><li>For Patients</li><li>Our Physicians</li><li>For Physicians</li><li>PACS &amp; Documents</li><li>Appointments</li><li>Our Locations</li>
  </ul>

  <!-- Contact details -->
  <svg class="abs" style="left:283px;top:3040px" width="42" height="38" viewBox="0 0 42 38"><path d="M3 10l12-6 12 6 12-6v24l-12 6-12-6-12 6z" fill="none" stroke="var(--green)" stroke-width="3"/></svg>
  <div class="abs f-head" style="left:283px;top:3090px">Contact <strong>Details</strong></div>
  <svg class="abs" style="left:283px;top:3128px" width="14" height="18" viewBox="0 0 14 18"><path d="M7 17s6-7 6-10A6 6 0 001 7c0 3 6 10 6 10z" fill="var(--green)"/><circle cx="7" cy="7" r="2" fill="var(--footer)"/></svg>
  <div class="abs f-text" style="left:318px;top:3122px">PVIP P.C.,<br>Dollar smit, City Code-1234</div>
  <svg class="abs" style="left:283px;top:3190px" width="16" height="12" viewBox="0 0 16 12"><rect x="1" y="1" width="14" height="10" fill="none" stroke="var(--green)" stroke-width="2"/><path d="M1 1l7 6 7-6" fill="none" stroke="var(--green)" stroke-width="2"/></svg>
  <div class="abs f-text" style="left:318px;top:3182px">info@pvipmail.com</div>

  <!-- For patients -->
  <svg class="abs" style="left:283px;top:3242px" width="40" height="36" viewBox="0 0 40 36"><circle cx="14" cy="10" r="7" fill="none" stroke="var(--green)" stroke-width="3"/><path d="M2 34a12 12 0 0124 0" fill="none" stroke="var(--green)" stroke-width="3"/><path d="M28 14h10M33 9v10" stroke="var(--green)" stroke-width="3"/></svg>
  <div class="abs f-head" style="left:283px;top:3287px">For <strong>Patients</strong></div>
  <ul class="abs f-list" style="left:290px;top:3316px"><li>About Your Visit</li><li>Why Choose Us?</li></ul>
  <ul class="abs f-list" style="left:460px;top:3316px"><li>Patient Forms</li><li>Billing &amp; Insurance</li></ul>
  <ul class="abs f-list" style="left:620px;top:3316px"><li>Locations &amp; Maps</li><li>Appointments</li></ul>

  <!-- Contact us -->
  <svg class="abs" style="left:565px;top:3042px" width="40" height="34" viewBox="0 0 40 34"><rect x="2" y="2" width="36" height="30" fill="none" stroke="var(--green)" stroke-width="3"/><rect x="8" y="9" width="10" height="10" fill="var(--green)"/><path d="M22 10h10M22 16h10M8 25h24" stroke="var(--green)" stroke-width="3"/></svg>
  <div class="abs f-head" style="left:565px;top:3090px">Contact <strong>Us</strong></div>
  <div class="abs f-text" style="left:565px;top:3122px;font-size:12.5px">
    <span class="f-label">Main Line:</span><br><span class="f-label">Scheduling:</span><br><span class="f-label">Billing:</span><br><span class="f-label">Medical Records:</span>
  </div>
  <div class="abs f-text" style="left:680px;top:3122px">(555) 382-6633<br>(555) 382-9383<br>(555) 383-1614<br>(555) 383-5977</div>

  <!-- Hours -->
  <div class="abs hours">
    <svg class="abs" style="left:105px;top:14px" width="48" height="48" viewBox="0 0 48 48"><circle cx="24" cy="24" r="20" fill="none" stroke="var(--green)" stroke-width="4"/><path d="M24 12v12l-7 8" fill="none" stroke="var(--green)" stroke-width="4"/></svg>
    <table>
      <tr><td>MON:</td><td>8:30AM - 10:30 PM</td></tr>
      <tr><td>TUS:</td><td>1:00AM - 5:00 PM</td></tr>
      <tr><td>WED:</td><td>Free Day</td></tr>
      <tr><td>THR:</td><td>8:30AM - 12:30 PM</td></tr>
      <tr><td>FRI:</td><td>8:30AM - 12:00 PM</td></tr>
      <tr><td>SAT:</td><td>8:30AM - 10:30 PM</td></tr>
      <tr><td>SUN:</td><td>Free Day</td></tr>
    </table>
    <div class="abs hours-btn">Make An Appointment</div>
  </div>

  <div class="abs copyright">Copyright 2016 Pinecrest P.C. All Rights Reserved.</div>
</section>

</body>
</html>
```